Corbett Architecture (business card)

We need a business card design. We are a full service architectural firm that specializes in mostly residential projects and some commercial projects. We are located in Hudson Valley, New York. We work with high end clients and want a business card that is memorable and has a sleek, modern, design but will not go out of style (timeless).

Target Market(s)

high end residential clients

Industry/Entity Type

Architect

Contact Information for Business Card

Front of card
Company Logo
website: www.corbettdesignstudo.example
what we do: residential, Commercial

back of card
Owner's Name: Martin Corbett
owner's title: Principal
Business address: 2867 Orchard Lane Suite B, Maplethorpe, NY 10938
phone number: 845-555-0192
e-mail: mc@corbettdesignstudio.example

We like:
icons
sleek and clean design
simple not too busy or too much text

Font styles to use
Sans Serif

Colors
0356a4

Requirements
Must have
• company colors are navy blue, white, and gray
• Front of card
• Company Logo
• website: www.corbettdesignstudo.example
• what we do: residential, Commercial
• back of card
• Owner's Name: Martin Corbett
• owner's title: Principal
• Business address: 2867 Orchard Lane Suite B, Maplethorpe, NY 10938
• phone number: 845-555-0192
• e-mail: mc@corbettdesignstudio.example
Nice to have
• We like:
• icons
• sleek and clean design
• simple not too much text
• color of the card to be either blue or gray
Should not have
• we do not like houses in the design or plans of houses-this is over done and we don't like it.
• no QR CODES

```html
<!DOCTYPE html>
<html lang="en">
<head>
<meta charset="utf-8">
<title>Corbett Architecture – Business Card</title>
<link rel="stylesheet" href="https://fonts.googleapis.com/css2?family=Jost:wght@400&family=Roboto:wght@400;500;700&display=swap">
<style>
  :root {
    --navy: #242a7c;
    --gray: #7b7b7b;
    --gray-bar: #8a8a8a;
    --card: #f4f4f4;
    --backdrop: #b9b9b9;
    --white: #ffffff;
  }
  * { margin: 0; padding: 0; box-sizing: border-box; }
  html, body {
    width: 1200px; height: 576px; overflow: hidden;
    background: var(--backdrop);
    font-family: "Roboto", Arial, sans-serif;
  }
  .canvas { position: relative; width: 1200px; height: 576px; }
  .card {
    position: absolute;
    background: var(--card);
    border-radius: 12px;
    overflow: hidden;
    box-shadow: 0 4px 8px rgba(0,0,0,.25);
  }
  .card-front { left: 82px; top: 139px; width: 484px; height: 293px; }
  .card-back  { left: 602px; top: 138px; width: 481px; height: 291px; }

  .brand { position: absolute; display: flex; flex-direction: column; align-items: center; }
  .brand-mark { background: var(--navy); }
  .brand-name {
    font-family: "Jost", "Futura", sans-serif;
    font-weight: 400;
    color: var(--gray);
    text-transform: uppercase;
    text-align: center;
    line-height: 1.05;
    letter-spacing: 0.5px;
  }
  .card-front .brand { left: 0; right: 0; top: 46px; }
  .card-front .brand-mark { width: 46px; height: 46px; margin-bottom: 20px; }
  .card-front .brand-name { font-size: 30px; }

  .card-back .brand { left: 0; width: 262px; top: 78px; }
  .card-back .brand-mark { width: 56px; height: 56px; margin-bottom: 14px; }
  .card-back .brand-name { font-size: 24px; }

  .footer-shapes { position: absolute; left: 0; bottom: 0; }
  .website-front {
    position: absolute; left: 38px; top: 259px;
    font-size: 12.5px; color: var(--navy);
  }
  .services {
    position: absolute; left: 297px; top: 266px;
    font-size: 13px; color: var(--white);
  }

  .contact { position: absolute; left: 254px; top: 0; color: var(--navy); }
  .owner-name { position: absolute; top: 66px; font-size: 19px; font-weight: 700; white-space: nowrap; }
  .owner-title { position: absolute; top: 90px; font-size: 12.5px; color: var(--gray); white-space: nowrap; }
  .contact-list { position: absolute; top: 126px; list-style: none; font-size: 12.5px; }
  .contact-list li { display: flex; align-items: center; height: 18.5px; white-space: nowrap; }
  .contact-list svg { width: 11px; height: 11px; margin: 0 12px 0 4px; fill: var(--gray); }
  .address { position: absolute; top: 186px; font-size: 12.5px; line-height: 18.5px; white-space: nowrap; font-style: normal; }
</style>
</head>
<body>
<div class="canvas">
  <section class="card card-front">
    <div class="brand">
      <div class="brand-mark"></div>
      <div class="brand-name">Corbett<br>Architecture</div>
    </div>
    <svg class="footer-shapes" width="484" height="38" viewBox="0 0 484 38">
      <rect x="0" y="23" width="250" height="15" fill="var(--gray-bar)"/>
      <path d="M238 38 L256 6 Q259 0 266 0 L484 0 L484 38 Z" fill="var(--navy)"/>
    </svg>
    <p class="website-front">www.corbettdesignstudo.example</p>
    <p class="services">Residential &nbsp;|&nbsp; Commercial</p>
  </section>

  <section class="card card-back">
    <div class="brand">
      <div class="brand-mark"></div>
      <div class="brand-name">Corbett<br>Architecture</div>
    </div>
    <div class="contact">
      <h1 class="owner-name">Martin Corbett</h1>
      <p class="owner-title">Principal/Owner</p>
      <ul class="contact-list">
        <li><svg viewBox="0 0 12 12"><path d="M1 4 Q6 0 11 4 L10 5.5 L8 4.5 L8 3.5 Q6 2.8 4 3.5 L4 4.5 L2 5.5 Z M3 6 L9 6 L10.5 11 L1.5 11 Z"/></svg>845-555-0192</li>
        <li><svg viewBox="0 0 12 12"><path d="M0.5 2.5 H11.5 V9.5 H0.5 Z M1.5 3.5 L6 6.8 L10.5 3.5 Z" fill-rule="evenodd"/></svg>mc@corbettdesignstudio.example</li>
        <li><svg viewBox="0 0 12 12"><path d="M6 0.5 A5.5 5.5 0 1 0 6.01 0.5 Z M6 1.5 A4.5 4.5 0 1 1 5.99 1.5 Z M5.5 1.5 H6.5 V10.5 H5.5 Z M1.5 5.5 H10.5 V6.5 H1.5 Z" fill-rule="evenodd"/></svg>www.corbettdesignstudo.example</li>
      </ul>
      <address class="address">2867 Orchard Lane Suite B<br>Maplethorpe, NY 10938</address>
    </div>
  </section>
</div>
</body>
</html>
```